Business card for a "family office" company

Please provide professional looking business card designs, incorporating the attached logo and below details. Harrowmere Holdings Pty Ltd is a family office / financial investment company. We are looking for a modern, professional and contemporary card design.

Industry/Entity Type

Finance

Contact Information for Business Card

Name: Dean Mollick
Title: Director
Company: Harrowmere Holdings Pty Ltd
Email: harrowdean@quillnet.example
Mobile: 0462 735 418
Address: 4/312 Barnaby Parade, Cottesloe WA 6011, Australia

Requirements
Must have
• All details above and the logo. logo only on back side. incorporate colours of logo
Nice to have
• up to you
Should not have
• ?

```html
<!DOCTYPE html>
<html lang="en">
<head>
<meta charset="utf-8">
<title>Harrowmere Holdings – Business Card</title>
<link rel="stylesheet" href="https://fonts.googleapis.com/css2?family=Gelasio:wght@400;500&display=swap">
<style>
  :root {
    --navy: #201f55;
    --ink: #1f1d5a;
    --accent: #2c3794;
    --paper-light: #f4f4f5;
    --paper-mid: #e3e3e5;
    --paper-dark: #c9c9cc;
    --white: #ffffff;
    --serif: "Gelasio", Georgia, serif;
  }
  * { margin: 0; padding: 0; box-sizing: border-box; }
  html, body {
    width: 1200px; height: 329px; overflow: hidden; background: var(--white);
  }
  .sheet { position: relative; width: 1200px; height: 329px; font-family: var(--serif); }

  .card { position: absolute; top: 0; height: 329px; }
  .card--front {
    left: 0; width: 572px;
    background:
      linear-gradient(180deg, rgba(255,255,255,0) 60%, rgba(190,190,195,0.45) 85%, rgba(230,230,232,0.6) 100%),
      linear-gradient(90deg, var(--paper-dark) 0%, var(--paper-mid) 22%, var(--paper-light) 55%, var(--paper-mid) 100%);
  }
  .card--back { left: 627px; width: 573px; background: var(--navy); }

  .brand { position: absolute; display: flex; flex-direction: column; align-items: center; }
  .brand__mark { width: 26px; height: 26px; margin-bottom: 14px; }
  .brand__name {
    font-weight: 400; font-size: 22px; letter-spacing: 3px; line-height: 1.25;
    text-transform: uppercase; text-align: center;
  }
  .card--front .brand { left: 22px; top: 112px; width: 226px; }
  .card--front .brand__mark { background: var(--navy); }
  .card--front .brand__name { color: var(--navy); }
  .card--back .brand { left: 0; top: 112px; width: 573px; }
  .card--back .brand__mark { background: var(--white); }
  .card--back .brand__name { color: var(--white); font-size: 26px; letter-spacing: 4px; }

  .contact { position: absolute; left: 285px; top: 40px; color: var(--ink); }
  .contact__name { font-size: 37px; font-weight: 400; line-height: 1; }
  .contact__title { font-size: 21px; color: var(--accent); margin-top: 10px; }
  .contact__company { font-size: 19px; margin-top: 38px; }
  .contact__address { font-size: 15px; line-height: 20px; margin-top: 8px; font-style: normal; }
  .contact__line {
    display: flex; align-items: center; gap: 8px;
    font-size: 16.5px; color: var(--accent); margin-top: 5px; height: 22px;
  }
  .contact__line:first-of-type { margin-top: 6px; }
  .contact__icon { width: 22px; height: 22px; flex: none; }
</style>
</head>
<body>
<main class="sheet">
  <section class="card card--front">
    <div class="brand">
      <span class="brand__mark"></span>
      <span class="brand__name">Harrowmere<br>Holdings</span>
    </div>

    <div class="contact">
      <h1 class="contact__name">Dean Mollick</h1>
      <p class="contact__title">Director</p>
      <p class="contact__company">Harrowmere Holdings Pty Ltd.</p>
      <address class="contact__address">4/312 Barnaby Parade, Cottesloe<br>WA 6011, Australia.</address>
      <p class="contact__line">
        <svg class="contact__icon" viewBox="0 0 22 22" aria-hidden="true">
          <circle cx="11" cy="11" r="11" fill="var(--navy)"/>
          <path d="M7.2 5.5c.5-.4 1.1-.3 1.4.2l1.1 1.8c.3.5.2 1-.2 1.4l-.8.7c.6 1.4 1.7 2.6 3.2 3.3l.7-.8c.4-.4.9-.5 1.4-.2l1.8 1.1c.5.3.6.9.2 1.4l-.9 1c-.6.6-1.5.8-2.3.5-3-1.1-5.4-3.5-6.5-6.5-.3-.8-.1-1.7.5-2.3z" fill="var(--white)"/>
        </svg>
        <span>0462 735 418</span>
      </p>
      <p class="contact__line">
        <svg class="contact__icon" viewBox="0 0 22 22" aria-hidden="true">
          <rect x="0" y="4" width="22" height="14" fill="var(--navy)"/>
          <path d="M1.5 5.5 11 12.5l9.5-7M1.5 16.5l6.5-5.5M20.5 16.5 14 11" stroke="var(--white)" stroke-width="1.2" fill="none"/>
        </svg>
        <span>harrowdean@quillnet.example</span>
      </p>
    </div>
  </section>

  <section class="card card--back">
    <div class="brand">
      <span class="brand__mark"></span>
      <span class="brand__name">Harrowmere<br>Holdings</span>
    </div>
  </section>
</main>
</body>
</html>
```